Buddhist Center Advertisement

I need a full page single sided 8.5" by 11" flyer for posting around town that describes our upcoming schedule as well as general information about our center. The flyer should be full color and print at 300 DPI. I'm open to a variety of Buddhist imagery, but it should be related to Tibetan Buddhism.
The flyers will be read off bulletin boards so the text shouldn't be too small.
I prefer not to put text over semi-transparent graphics, I think it makes the text too difficult to read.
Target Market(s)
Spiritually minded people seeking instruction in meditation and looking for a new way of relating to themselves and the world, people looking for answers to life's most important questions. The main function of the flyer is to attract new members.
Industry/Entity Type
Town
Requirements
Must have
- 1. our schedule, with class description
Name of Module: "Opening the Lotus: Turning Hardship into Calm Joy"
In this module we will consider well the disadvantages of self-cherishing and the advantages of cherishing others more than ourselves. We will learn how to employ the special techniques of mind training or “lo-jong” as a means to transform problems into happiness, and learn to treat our challenges as precious opportunities for spiritual growth.
Saturday, September 21 10:30 - 12:30
Saturday, September 28 10:30 - 12:30
Saturday, October 26 10:30 - 12:30
Saturday, November 9 10:30 - 6:00 Retreat Day
Saturday, November 23 10:30 - 6:00 Retreat Day
2. Our website, www.velmarodhi.org
3. our phone number (555) 318-2047
4. Our facebook and Gatherlane pages
www.circlepage.com/VelmarodhiCenter
www.gatherlane.com/velmarodhi-buddhist-center
5. This text
"The Velmarodhi center is a community of spiritual friends dedicated to the practice of Tibetan Buddhism. We practice in the Gelugpa tradition, the same lineage as his Holiness The Venerable Ketsun. The Center was founded in 1994 under the spiritual direction of Lama Tenkar Norbu, and the Society for the Continuance of the Lotus Path Teachings. We offer weekly classes in meditation and Buddhist philosophy suitable for beginners as well as advanced practitioners. All classes are free of charge and offered on a donation basis only.
Nice to have
- our logo

```html
<!DOCTYPE html>
<html lang="en">
<head>
<meta charset="utf-8">
<title>Opening the Lotus – Velmarodhi Center Flyer</title>
<link href="https://fonts.googleapis.com/css2?family=Roboto+Condensed:wght@400;700&family=Oswald:wght@500;600&family=Great+Vibes&display=swap" rel="stylesheet">
<style>
  :root {
    --backdrop: #4b4b4b;
    --sky-top: #2f6fb6;
    --sky-mid: #8fb6d8;
    --glow: #f7d97a;
    --saffron: #ffc43c;
    --saffron-deep: #ff9a2c;
    --ribbon: #f0691a;
    --lotus-yellow: #f4ea12;
    --ink: #3b2a0e;
    --ink-soft: #5a3c12;
    --icon: #e07a18;
    --white: #ffffff;
  }
  * { box-sizing: border-box; margin: 0; padding: 0; }
  html, body { width: 1200px; height: 1000px; overflow: hidden; }
  body { background: var(--backdrop); position: relative; font-family: "Roboto Condensed", sans-serif; }
  ul { list-style: none; }

  .flyer {
    position: absolute; left: 227px; top: 15px; width: 748px; height: 970px;
    background: linear-gradient(180deg, var(--saffron) 52%, var(--saffron-deep) 100%);
    overflow: hidden;
  }
  .hero-art {
    position: absolute; left: 0; top: 0; width: 748px; height: 510px;
    background:
      radial-gradient(ellipse 220px 300px at 360px 250px, #e96a12 0%, #f08a2a 45%, rgba(247,217,122,0.6) 70%, rgba(247,217,122,0) 100%),
      linear-gradient(180deg, var(--sky-top) 0%, var(--sky-mid) 55%, var(--glow) 80%, var(--saffron) 100%);
  }

  .ribbon { position: absolute; left: 62px; top: 0; width: 103px; height: 212px; }
  .ribbon-text {
    position: absolute; left: 74px; top: 50px; width: 86px;
    font-family: "Oswald", sans-serif; font-weight: 500; color: var(--white);
    font-size: 11.5px; line-height: 13px; text-transform: uppercase; white-space: nowrap;
  }
  .ribbon-text span { display: block; }
  .ribbon-text .big { font-size: 17px; line-height: 18px; }

  .title-disc {
    position: absolute; left: 421px; top: 185px; width: 292px; height: 292px; border-radius: 50%;
    background: linear-gradient(180deg, rgba(70,58,12,0.88) 0%, rgba(120,70,10,0.9) 45%, #e8530f 70%, #f06a14 100%);
    text-align: center; color: var(--white);
  }
  .title-script { font-family: "Great Vibes", cursive; font-size: 46px; line-height: 1; margin-top: 58px; font-weight: 400; }
  .title-main { font-family: "Oswald", sans-serif; font-weight: 600; font-size: 56px; line-height: 1; color: var(--lotus-yellow); letter-spacing: 0.5px; margin-top: 2px; }
  .title-rule { width: 218px; height: 1px; background: var(--white); margin: 14px auto 10px; opacity: 0.85; }
  .title-sub { font-size: 22px; line-height: 24px; }
  .title-sub .into { color: var(--lotus-yellow); }
  .title-sub .script { font-family: "Great Vibes", cursive; font-size: 34px; color: var(--lotus-yellow); }

  .schedule { position: absolute; left: 120px; top: 488px; width: 200px; text-align: center; color: var(--ink-soft); }
  .session { margin-bottom: 4px; }
  .session-date { font-size: 14px; line-height: 16px; }
  .session-time { font-size: 16px; line-height: 19px; font-weight: 700; color: var(--ink); }

  .module-desc {
    position: absolute; left: 343px; top: 488px; width: 270px;
    font-size: 15px; line-height: 21.6px; color: var(--ink);
  }
  .module-desc .line { display: block; white-space: nowrap; text-align: justify; text-align-last: justify; }
  .module-desc .line.last { text-align-last: left; }
  .module-desc strong { font-weight: 700; }

  .divider { position: absolute; left: 135px; top: 696px; width: 478px; height: 12px; }

  .center-mark { position: absolute; left: 128px; top: 728px; width: 118px; text-align: center; }
  .center-mark-circle { width: 92px; height: 92px; border-radius: 50%; border: 2px solid var(--white); margin: 0 auto 6px; }
  .center-mark-name { font-size: 15px; color: var(--white); font-weight: 700; }

  .about {
    position: absolute; left: 254px; top: 720px; width: 360px;
    font-size: 12.4px; line-height: 20.4px; color: var(--ink); text-align: justify; hyphens: auto;
  }
  .about .org { font-weight: 700; text-transform: uppercase; }

  .contact-primary { position: absolute; left: 60px; top: 875px; font-weight: 700; font-size: 21px; color: var(--ink); }
  .contact-primary li { display: flex; align-items: center; height: 30px; }
  .contact-primary svg { width: 20px; height: 20px; margin-right: 11px; }

  .contact-social { position: absolute; left: 383px; top: 876px; font-size: 13.5px; color: var(--ink); }
  .contact-social li { display: flex; align-items: center; height: 32px; }
  .social-square { width: 26px; height: 26px; background: var(--white); margin-right: 10px; border-radius: 2px; }
  .contact-social b { font-weight: 700; }
</style>
</head>
<body>
  <main class="flyer">
    <div class="hero-art" role="img" aria-label="Golden seated Buddha statue glowing against a blue sky with sun rays and clouds, lotus silhouettes along the bottom"></div>

    <svg class="ribbon" viewBox="0 0 103 212" aria-hidden="true">
      <path d="M0 0 H103 V212 L51.5 160 L0 212 Z" fill="var(--ribbon)"/>
      <path d="M6 0 V196 M97 0 V196" stroke="#ffd2a8" stroke-width="1" stroke-dasharray="3 3" fill="none"/>
    </svg>
    <p class="ribbon-text">
      <span>All classes are</span>
      <span>free of charge</span>
      <span>and offered on</span>
      <span class="big">a donation</span>
      <span class="big">basis only.</span>
    </p>

    <section class="title-disc">
      <h1>
        <div class="title-script">Opening the</div>
        <div class="title-main">LOTUS</div>
      </h1>
      <div class="title-rule"></div>
      <p class="title-sub">Turning Hardship<br><span class="into">into</span> <span class="script">Calm Joy</span></p>
    </section>

    <ul class="schedule">
      <li class="session"><div class="session-date">Saturday, September 21, 2013</div><div class="session-time">10:30 - 12:30</div></li>
      <li class="session"><div class="session-date">Saturday, September 28, 2013</div><div class="session-time">10:30 - 12:30</div></li>
      <li class="session"><div class="session-date">Saturday, October 26, 2013</div><div class="session-time">10:30 - 12:30</div></li>
      <li class="session"><div class="session-date">Saturday, November 9, 2013</div><div class="session-time">10:30 - 6:00 &nbsp;RETREAT DAY</div></li>
      <li class="session"><div class="session-date">Saturday, November 23, 2013</div><div class="session-time">10:30 - 6:00 &nbsp;RETREAT DAY</div></li>
    </ul>

    <p class="module-desc">
      <span class="line">In this module we will consider well the</span>
      <span class="line">disadvantages of self-cherishing and the</span>
      <span class="line">advantages of cherishing others more</span>
      <span class="line">than ourselves. We will learn how to em-</span>
      <span class="line">ploy the special techniques of mind train-</span>
      <span class="line">ing or “<strong>lo-jong</strong>” as a means to transform</span>
      <span class="line">problems into happiness, and learn to</span>
      <span class="line">treat our challenges as precious opportu-</span>
      <span class="line last">nities for spiritual growth.</span>
    </p>

    <svg class="divider" viewBox="0 0 478 12" aria-hidden="true">
      <line x1="0" y1="6" x2="478" y2="6" stroke="var(--white)" stroke-width="1"/>
      <rect x="234" y="1" width="10" height="10" fill="var(--white)" transform="rotate(45 239 6)"/>
    </svg>

    <div class="center-mark">
      <div class="center-mark-circle"></div>
      <div class="center-mark-name">Velmarodhi</div>
    </div>

    <p class="about"><span class="org">The Velmarodhi Center</span> is a community of spiritual friends dedicated to the practice of Tibetan Buddhism. We practice in the Gelugpa tradition, the same lineage as his Holiness The Venerable Ketsun. The Center was founded in 1994 under the spiritual direction of Lama Tenkar Norbu, and the Society for the Continuance of the Lotus Path Teachings. We offer weekly classes in meditation and Buddhist philosophy suitable for beginners as well as advanced practitioners.</p>

    <ul class="contact-primary">
      <li><svg viewBox="0 0 20 20" aria-hidden="true"><circle cx="10" cy="10" r="8" fill="var(--icon)"/><path d="M6 10 H14 M11 7 L14 10 L11 13" stroke="var(--white)" stroke-width="2" fill="none"/></svg>www.velmarodhi.org</li>
      <li><svg viewBox="0 0 20 20" aria-hidden="true"><path d="M5 3 L8 3 L9 7 L7 8.5 C8 11 9 12 11.5 13 L13 11 L17 12 L17 15 C17 16 16 17 15 17 C9 17 3 11 3 5 C3 4 4 3 5 3 Z" fill="var(--icon)"/></svg>(555) 318-2047</li>
    </ul>

    <ul class="contact-social">
      <li><span class="social-square"></span>www.circlepage.com/<b>VelmarodhiCenter</b></li>
      <li><span class="social-square"></span>www.gatherlane.com/<b>velmarodhi-buddhist-center</b></li>
    </ul>
  </main>
</body>
</html>
```